Nobre Lente Lusitana - business card

Create a business card for my eyewear (glasses) store. The concept is based in handcrafted glasses (as well as common frames and 3d printed), clean, and elegant. The business card could be black (white letters and symbols) or white (black letters and symbols) but we are open to new suggestions. It must be sober and elegant.
The name Nobre Lente Lusitana means Royal/Real Portuguese Optical Store.
Our concept should be inspired by the pictures attatched bellow.
I would like it to be classic and elegant as business cards for bankers.
Our first selected logo is also available in attachment files.

Target Market(s)

For business meetings with investors, supliers and fairs

Industry/Entity Type

Eyewear

Contact Information for Business Card

Some random business cards in attachment that we like. Don't be closed to it, we like freedom of think.

Font styles to use
Serif
Sans Serif

Colors
404040
e9e9e9
fbfbfb
000000
85abd3
0255a3
f7fbfd
959595

Requirements
Must have
• Must be elegant, simple.
• Must present our brand new logo (slight variations are welcome, the logo is not closed yet). See our temporary logo in attachment.
• Black (or dark grey), white (or light grey) and a third slight color.
• This third slight color could be dark blue or grayish blue.
• Info:
• Tomás Vidigal (name)
• tvidigal@nobrelentelusitana.example
• +351 927364051
• www.nobrelentelusitana.example
Nice to have
• Black and white or with serious colors such as dark blue or greyish blue.
• Could also have water mark with our logo (big size) in the background (inspired in KMT bank credit card design)
Should not have
• Hysteric colora or shapes

```html
<!DOCTYPE html>
<html lang="pt">
<head>
<meta charset="utf-8">
<title>Nobre Lente Lusitana – Cartão de visita</title>
<link rel="stylesheet" href="https://fonts.googleapis.com/css2?family=Jost:wght@400;700&display=swap">
<style>
  :root {
    --backdrop: #8e8f92;
    --card-ink: #0b1117;
    --card-navy: #12202c;
    --text-light: #f7fbfd;
  }
  * { margin: 0; padding: 0; box-sizing: border-box; }
  html, body {
    width: 1200px;
    height: 638px;
    overflow: hidden;
    background: var(--backdrop);
    font-family: "Jost", "Futura", sans-serif;
  }
  .business-card {
    position: absolute;
    left: 160px;
    top: 67px;
    width: 880px;
    height: 503px;
    overflow: hidden;
    background: var(--card-ink);
  }
  .damask-pattern {
    position: absolute;
    inset: 0;
    background:
      radial-gradient(ellipse at 25% 30%, rgba(30, 52, 70, 0.55), transparent 60%),
      radial-gradient(ellipse at 80% 75%, rgba(26, 46, 62, 0.5), transparent 60%),
      linear-gradient(135deg, var(--card-navy), var(--card-ink));
  }
  .brand-name {
    position: absolute;
    left: 70px;
    top: 126px;
    width: 300px;
    text-align: center;
    color: var(--text-light);
    font-weight: 400;
    font-size: 28px;
    line-height: 1.25;
  }
  .contact-block {
    position: absolute;
    left: 296px;
    top: 262px;
    color: var(--text-light);
  }
  .holder-name {
    font-weight: 700;
    font-size: 36px;
    letter-spacing: 0.5px;
    margin-bottom: 18px;
    margin-left: 16px;
  }
  .contact-list { list-style: none; }
  .contact-item {
    display: flex;
    align-items: center;
    gap: 18px;
    font-size: 22px;
    letter-spacing: 0.6px;
    height: 40px;
  }
  .contact-icon {
    width: 26px;
    height: 26px;
    flex: none;
  }
</style>
</head>
<body>
  <main class="business-card">
    <div class="damask-pattern" role="img" aria-label="Padrão floral damasco em azul escuro sobre fundo preto"></div>

    <div class="brand-name">Nobre Lente<br>Lusitana</div>

    <section class="contact-block">
      <h1 class="holder-name">Tomás Vidigal</h1>
      <ul class="contact-list">
        <li class="contact-item">
          <svg class="contact-icon" viewBox="0 0 26 26" aria-hidden="true">
            <rect x="2" y="6" width="22" height="15" fill="none" stroke="#f7fbfd" stroke-width="2"/>
            <path d="M2 6 L13 15 L24 6" fill="none" stroke="#f7fbfd" stroke-width="2"/>
          </svg>
          <span>tvidigal@nobrelentelusitana.example</span>
        </li>
        <li class="contact-item">
          <svg class="contact-icon" viewBox="0 0 26 26" aria-hidden="true">
            <circle cx="13" cy="13" r="12" fill="#f7fbfd"/>
            <path d="M9 7 L11 7 L12 10 L10.5 11.5 Q12 15 14.5 16 L16 14.5 L19 15.5 L19 17.5 Q17 20 14 18.5 Q8 15 7.5 9.5 Q7.5 7.5 9 7 Z" fill="#0b1117"/>
          </svg>
          <span>+351 927364051</span>
        </li>
        <li class="contact-item">
          <svg class="contact-icon" viewBox="0 0 26 26" aria-hidden="true">
            <circle cx="11" cy="11" r="9" fill="none" stroke="#f7fbfd" stroke-width="1.8"/>
            <ellipse cx="11" cy="11" rx="4" ry="9" fill="none" stroke="#f7fbfd" stroke-width="1.4"/>
            <path d="M2 11 H20 M4 6 H18 M4 16 H18" stroke="#f7fbfd" stroke-width="1.2"/>
            <path d="M17.5 17.5 L24 24" stroke="#f7fbfd" stroke-width="3" stroke-linecap="round"/>
          </svg>
          <span>www.nobrelentelusitana.example</span>
        </li>
      </ul>
    </section>
  </main>
</body>
</html>
```